Finance Broker helping people meet their personal and business goals

New business card design,
1st look at the old business card so this makes sense.
I DON'T want:
the subtext "For all your Rural and Commercial Finance".
I DON'T want the: "and Management Consultant" words
I DON'T want the old phone: 07 48213957
I DON'T want the fax number: 07 45826031
I DON'T want the email address: tallowcreek@brightlink.com.au
I DON'T want the flower
What I DO want
I DO want the mobile 0451 836 209 (in larger text)
I DO want:
My name: Dennis Harwell-Lowe
I DO want: Australian Credit Licence 529164 (Tallow Creek Pty Ltd)
I DO want: Principal Finance Broker
I DO want new email: dennis@plotnextstep.com.au
I DO want address: PO Box 928, Tully Qld 4854
I DO want the existing logo (PNS on existing card)

Target Market(s)

Business Borrowers, Home Purchasers, and People wanting to finance cars and plant and equipment

Industry/Entity Type

Financial Service

Contact Information for Business Card

See project description

Font styles to use
Serif

Colors

Designer to choose colors to be used in the design.

Requirements
Must have
• See project description
Nice to have
• Black and Yellow colours
Should not have
• See project description

```html
<!DOCTYPE html>
<html lang="en">
<head>
<meta charset="utf-8">
<title>Plot Next Step – Business Card</title>
<link rel="stylesheet" href="https://fonts.googleapis.com/css2?family=Kalam:wght@400;700&family=Crimson+Pro:wght@400;600&display=swap">
<style>
  :root {
    --backdrop: #7a5a3c;
    --card-black: #0b0b0b;
    --card-edge: #2a2a2a;
    --accent-yellow: #f2ec16;
    --text-white: #f4f4f4;
    --font-script: "Kalam", cursive;
    --font-serif: "Crimson Pro", serif;
  }
  * { margin: 0; padding: 0; box-sizing: border-box; }
  html, body {
    width: 900px; height: 1200px; overflow: hidden;
    background: var(--backdrop);
  }
  .canvas { position: relative; width: 900px; height: 1200px; }

  .business-card {
    position: absolute;
    width: 731px; height: 428px;
    border-radius: 22px;
    background: linear-gradient(35deg, var(--card-edge) 0%, var(--card-black) 45%, var(--card-black) 100%);
    box-shadow: 0 6px 14px rgba(0,0,0,0.45);
    color: var(--text-white);
  }
  .business-card--front { left: 82px; top: 128px; }
  .business-card--back  { left: 80px; top: 646px; }

  .rule {
    position: absolute; height: 4px; border-radius: 2px;
    background: var(--accent-yellow);
  }
  .rule--top-left  { left: 28px;  top: 46px; width: 252px; }
  .rule--top-right { left: 446px; top: 46px; width: 254px; }
  .rule--bottom    { left: 28px;  top: 381px; width: 674px; }

  .brand-mark {
    position: absolute; left: 280px; top: 28px; width: 166px; height: 40px;
    display: flex; align-items: center; justify-content: center; gap: 8px;
  }
  .brand-mark__dot { width: 22px; height: 22px; border-radius: 50%; background: var(--accent-yellow); }
  .brand-mark__name {
    font-family: var(--font-serif); font-weight: 600; font-size: 30px;
    color: var(--accent-yellow); letter-spacing: 2px; line-height: 1;
  }

  .line {
    position: absolute; left: 0; right: 0; text-align: center; white-space: nowrap;
  }
  .company-name {
    top: 96px; font-family: var(--font-serif); font-weight: 600;
    font-size: 31px; line-height: 36px; color: var(--accent-yellow);
  }
  .company-tagline {
    top: 134px; font-family: var(--font-script); font-size: 16px; line-height: 20px;
  }
  .person-name {
    top: 164px; font-family: var(--font-script); font-size: 33px; line-height: 42px;
  }
  .licence {
    top: 207px; font-family: var(--font-serif); font-size: 18px; line-height: 22px;
  }
  .job-title {
    top: 230px; font-family: var(--font-serif); font-size: 18px; line-height: 22px;
  }
  .mobile {
    top: 266px; font-family: var(--font-serif); font-size: 30px; line-height: 36px;
  }
  .email {
    top: 299px; font-family: var(--font-serif); font-size: 18px; line-height: 22px;
  }
  .postal {
    top: 326px; font-family: var(--font-serif); font-size: 18px; line-height: 22px;
  }
</style>
</head>
<body>
<main class="canvas">

  <section class="business-card business-card--front">
    <span class="rule rule--top-left"></span>
    <div class="brand-mark"><span class="brand-mark__dot"></span><span class="brand-mark__name">PNS</span></div>
    <span class="rule rule--top-right"></span>
    <p class="line company-name">Plot Next Step</p>
    <p class="line company-tagline">A Member of the Tallow Creek Group</p>
    <p class="line person-name">Dennis Harwell-Lowe</p>
    <p class="line licence">Australian Credit Licence 529164 (Tallow Creek Pty Ltd)</p>
    <p class="line job-title">Principal Finance Broker</p>
    <p class="line mobile">0451 836 209</p>
    <p class="line email">dennis@plotnextstep.com.au</p>
    <p class="line postal">PO Box 928, Tully Qld 4854</p>
    <span class="rule rule--bottom"></span>
  </section>

  <section class="business-card business-card--back">
    <span class="rule rule--top-left"></span>
    <div class="brand-mark"><span class="brand-mark__dot"></span><span class="brand-mark__name">PNS</span></div>
    <span class="rule rule--top-right"></span>
    <p class="line company-name">Plot Next Step</p>
    <p class="line company-tagline">A Member of the Tallow Creek Group</p>
    <p class="line person-name">Dennis Harwell-Lowe</p>
    <p class="line licence">Australian Credit Licence 529164 (Tallow Creek Pty Ltd)</p>
    <p class="line job-title">Principal Finance Broker</p>
    <p class="line mobile">0451 836 209</p>
    <p class="line email">dennis@plotnextstep.com.au</p>
    <p class="line postal">PO Box 928, Tully Qld 4854</p>
    <span class="rule rule--bottom"></span>
  </section>

</main>
</body>
</html>
```